Lease-A-Goose's web page

I need a web page(s) to show and promote my business of renting chickens. We provide seasonal rentals in the United States of a layer hen package for people who would like to try raising their own chickens. The package includes two hens, coop, attached run, feeder, waterer, and food. I would like interested people to be able to fill out a form so that I can have partners contact them to set up a delivery in their area. Our service is very popular with urban and suburban families.

Target Market(s)

Urban foodies.
Families.
People interested in Organic Foods.
People concerned with where their food comes from and how it is grown/prepared.
People interested in Urban Farming.

Industry/Entity Type

Business

Requirements
Must have
• A way for me to see rental interest based on zip code.
• A contact form including zip code, e-mail, and optional phone number.
• Our Logo. (Please contact if you are unable to use the file I provided.)
Nice to have
• A guest book for former renters that we can vet before posting.

```html
<!DOCTYPE html>
<html lang="en">
<head>
<meta charset="utf-8">
<title>Lease-A-Goose</title>
<link rel="stylesheet" href="https://fonts.googleapis.com/css2?family=Open+Sans:wght@400;600&display=swap">
<style>
:root{
  --green:#abc93a;
  --green-dark:#8aa82a;
  --nav-text:#6b7a2a;
  --ink:#555;
  --ink-soft:#777;
  --line:#cfcfcf;
  --page:#f2f2f2;
  --white:#fff;
}
*{box-sizing:border-box;margin:0;padding:0}
html,body{width:823px;height:1200px;overflow:hidden}
body{position:relative;background:var(--page);font-family:"Open Sans",Arial,sans-serif;color:var(--ink)}
.abs{position:absolute}
.topbar{top:9px;right:12px;font-size:12px;color:var(--ink);display:flex;align-items:center;gap:6px}
.social{width:14px;height:14px;background:#3b5998;border-radius:2px;display:inline-block}
.social.alt{background:#55acee}
.nav{top:33px;left:0;width:823px;height:37px;background:var(--green);border-top:1px solid #7e9a22;border-bottom:1px solid #7e9a22}
.brand{top:10px;left:10px;width:101px;height:76px;background:var(--white);border:2px solid var(--green-dark);border-radius:8px;display:flex;flex-direction:column;align-items:center;justify-content:center;gap:4px}
.brand-dot{width:30px;height:30px;border-radius:50%;background:var(--green)}
.brand-name{font-size:10px;font-weight:600;color:#c8301e}
.menu{top:8px;left:115px;display:flex;align-items:center;font-size:13px;color:var(--nav-text)}
.menu span{margin-right:21px}
.menu .active{width:68px;height:21px;border:1px solid #f2f2f2;border-radius:3px;background:#94b52c;color:#fff;display:flex;align-items:center;justify-content:center;margin-right:10px}
.search{top:7px;left:624px;width:188px;height:22px;background:#c7dc77;border:1px solid #8aa82a;border-radius:3px;font-size:12px;color:#fff;padding:2px 8px}
.search svg{position:absolute;right:8px;top:4px}
.slider{top:104px;left:9px;width:805px;height:299px;border-radius:8px;overflow:hidden;background:linear-gradient(160deg,#7c8a5a 0%,#8a5a2c 35%,#6c8b3a 65%,#4f7a2a 100%)}
.slide-title{top:76px;left:58px;font-size:34px;line-height:37px;color:#fff}
.slide-sub{top:163px;left:60px;font-size:15.5px;line-height:18px;color:#fff;width:320px}
.read-more{top:222px;left:60px;width:120px;height:34px;border:2px solid #fff;color:#fff;font-size:16px;display:flex;align-items:center;justify-content:center;gap:10px}
.arrow{top:129px;width:42px;height:41px;background:var(--green);display:flex;align-items:center;justify-content:center}
.dots{top:279px;left:370px;display:flex;gap:4px}
.dots i{width:13px;height:13px;border-radius:50%;background:#fff;display:block}
.dots i.on{background:var(--green)}
.card{top:453px;width:189px;height:229px;background:#fafafa;border:1px solid #e8e8e8}
.card-img{height:126px}
.card-title{height:43px;display:flex;align-items:center;justify-content:center;font-size:16px;color:var(--ink);background:#ebebeb}
.card.active .card-title{background:var(--green);color:#fff}
.card.active{border-bottom:3px solid var(--green)}
.card-text{padding:4px 16px;font-size:10px;line-height:15.5px;color:var(--ink-soft)}
.divider{top:717px;left:9px;width:805px;height:1px;background:#e2e2e2}
.vdivider{top:731px;left:477px;width:1px;height:356px;background:#e2e2e2}
.welcome{top:726px;left:10px;font-size:26px;color:var(--ink)}
.welcome-img{top:766px;left:9px;width:462px;height:212px;border:1px solid #bbb;background:#ddd;padding:4px}
.welcome-img div{width:100%;height:100%;background:linear-gradient(120deg,#d9d0c0,#a9825a 55%,#6d6a4c)}
.welcome-text{top:985px;left:10px;width:462px;font-size:15.5px;line-height:20.6px;color:var(--ink)}
.form-head{top:731px;left:488px;width:326px;height:30px;background:var(--green);border:1px solid var(--green-dark);color:#fff;font-size:17px;display:flex;align-items:center;justify-content:center}
.field{height:31px;background:#fff;border:1px solid #999;font-size:10.5px;color:var(--ink);display:flex;align-items:center;padding-left:11px}
.select-btn{position:absolute;right:0;top:0;width:29px;height:100%;background:var(--green);display:flex;align-items:center;justify-content:center}
.field svg.ic{position:absolute;right:9px}
.delivery{top:968px;left:487px;font-size:17px;color:var(--ink)}
.submit{top:1044px;left:488px;width:172px;height:25px;background:var(--green);color:#fff;font-size:10.5px;display:flex;align-items:center;justify-content:center;gap:18px}
.footer{top:1157px;left:0;width:823px;height:43px;background:var(--green);display:flex;align-items:center;justify-content:center;font-size:12.5px;color:#5c6b22}
</style>
</head>
<body>
<div class="abs topbar">
  <svg width="13" height="13" viewBox="0 0 24 24"><path fill="#555" d="M6.6 10.8a15.1 15.1 0 0 0 6.6 6.6l2.2-2.2c.3-.3.7-.4 1-.2 1.1.4 2.3.6 3.6.6.6 0 1 .4 1 1V20c0 .6-.4 1-1 1A17 17 0 0 1 3 4c0-.6.4-1 1-1h3.5c.6 0 1 .4 1 1 0 1.3.2 2.5.6 3.6.1.3 0 .7-.2 1z"/></svg>
  <span>Call Us:555-204-318&nbsp;|&nbsp; Follow Us:</span>
  <span class="social"></span><span class="social alt"></span>
</div>

<nav class="abs nav">
  <div class="abs menu">
    <span class="active">Home</span>
    <span>Packages &amp; Supplies</span>
    <span>Rent Chicken</span>
    <span>Services</span>
    <span>About</span>
    <span>Contact</span>
  </div>
  <div class="abs search">Search...
    <svg width="13" height="13" viewBox="0 0 24 24"><circle cx="10" cy="10" r="7" fill="none" stroke="#555" stroke-width="3"/><path d="M15 15l6 6" stroke="#555" stroke-width="3"/></svg>
  </div>
</nav>

<div class="abs brand"><span class="brand-dot"></span><span class="brand-name">LEASE-A-GOOSE</span></div>

<section class="abs slider" role="img" aria-label="Photo of a brown hen with chicks on grass">
  <h1 class="abs slide-title" style="font-weight:400">Lorem ipsum dolor sit amet,<br>suscipit nec wisi tincidunt.</h1>
  <p class="abs slide-sub">Lorem ipsum dolor sit amet, suscipit nec wisi tincidunt.</p>
  <div class="abs read-more">Read More
    <svg width="8" height="12" viewBox="0 0 8 12"><path d="M1 1l5 5-5 5" fill="none" stroke="#fff" stroke-width="2"/></svg>
  </div>
  <div class="abs arrow" style="left:0"><svg width="12" height="22" viewBox="0 0 12 22"><path d="M11 1L1 11l10 10" fill="none" stroke="#7e9a22" stroke-width="1.5"/></svg></div>
  <div class="abs arrow" style="right:0"><svg width="12" height="22" viewBox="0 0 12 22"><path d="M1 1l10 10-10 10" fill="none" stroke="#7e9a22" stroke-width="1.5"/></svg></div>
  <div class="abs dots"><i class="on"></i><i></i><i></i><i></i></div>
</section>

<article class="abs card active" style="left:9px">
  <div class="card-img" role="img" aria-label="Photo of yellow chicks" style="background:linear-gradient(135deg,#f0c46a,#d88a2a)"></div>
  <div class="card-title">Hatch Your Own Chicks</div>
  <p class="card-text">Lorem ipsum dolor sit amet, nulla amet ultricies sed wisi vitae ullamcorper.</p>
</article>
<article class="abs card" style="left:214px">
  <div class="card-img" role="img" aria-label="Photo of a black hen" style="background:linear-gradient(135deg,#8a8f7a,#2c2a3a)"></div>
  <div class="card-title">Chickens for Rent</div>
  <p class="card-text">Lorem ipsum dolor sit amet, nulla amet ultricies sed wisi vitae ullamcorper.</p>
</article>
<article class="abs card" style="left:420px">
  <div class="card-img" role="img" aria-label="Photo of a wooden chicken coop with run" style="background:linear-gradient(135deg,#c9c2a4,#6f7f4a)"></div>
  <div class="card-title">Coop Features</div>
  <p class="card-text">Lorem ipsum dolor sit amet, nulla amet ultricies sed wisi vitae ullamcorper.</p>
</article>
<article class="abs card" style="left:626px">
  <div class="card-img" role="img" aria-label="Photo of fresh eggs in a box" style="background:linear-gradient(135deg,#4a2a1e,#d98a5a 60%,#4a7a2a)"></div>
  <div class="card-title">Collect Fresh Eggs</div>
  <p class="card-text">Lorem ipsum dolor sit amet, nulla amet ultricies sed wisi vitae ullamcorper.</p>
</article>

<div class="abs divider"></div>
<div class="abs vdivider"></div>

<h2 class="abs welcome" style="font-weight:400">Welcome To Lease A Goose</h2>
<div class="abs welcome-img"><div role="img" aria-label="Photo of a hen with a group of chicks"></div></div>
<p class="abs welcome-text">Lorem Ipsum is simply dummy text of the printing and typeset-ting industry. Lorem Ipsum has been the industry's standard dummy text ever since the 1500s, when an unknown printer took a galley of type and scrambled it to make a type specimen book. It has survived not only five centuries,</p>

<form>
  <div class="abs form-head">Order Form</div>
  <div class="abs field" style="top:774px;left:488px;width:189px">Full Name</div>
  <div class="abs field" style="top:774px;left:694px;width:120px">Select Type
    <span class="select-btn"><svg width="12" height="8" viewBox="0 0 12 8"><path d="M1 1l5 5 5-5" fill="none" stroke="#333" stroke-width="2.2"/></svg></span>
  </div>
  <div class="abs field" style="top:812px;left:488px;width:326px">Address...</div>
  <div class="abs field" style="top:851px;left:488px;width:120px">City</div>
  <div class="abs field" style="top:851px;left:626px;width:188px">State</div>
  <div class="abs field" style="top:892px;left:488px;width:120px">Zip Code</div>
  <div class="abs field" style="top:892px;left:626px;width:188px">Phone Number</div>
  <div class="abs field" style="top:932px;left:488px;width:326px">Email..</div>
  <div class="abs delivery">Delivery:</div>
  <div class="abs field" style="top:998px;left:488px;width:155px">Desired delivery date:
    <svg class="ic" width="16" height="16" viewBox="0 0 16 16"><rect x="1" y="3" width="14" height="12" fill="none" stroke="#555" stroke-width="1.5"/><path d="M1 6h14M4 1v3M12 1v3" stroke="#555" stroke-width="1.5"/></svg>
  </div>
  <div class="abs field" style="top:998px;left:660px;width:154px">Desired delivery time:
    <svg class="ic" width="16" height="16" viewBox="0 0 16 16"><circle cx="8" cy="8" r="6.5" fill="none" stroke="#555" stroke-width="1.5"/><path d="M8 4v4l3 2" fill="none" stroke="#555" stroke-width="1.5"/></svg>
  </div>
  <div class="abs submit">Make Appointment
    <svg width="6" height="10" viewBox="0 0 6 10"><path d="M1 1l4 4-4 4" fill="none" stroke="#fff" stroke-width="1.5"/></svg>
  </div>
</form>

<footer class="abs footer">Copyrights © 2013 Lease A Goose.</footer>
</body>
</html>
```